Dental Business Card

I need Dental oriented business cards.
On the front side -
- on the first line, my name:
Dr Marlo Vintner
- on the second line (just underneath):
Doctor of Dental Medicine
- on the third line, or underneath that or in a corner, I would like the address and phone number:
5182 Ch. Birchfield
Montreal QC H2T 4B9
514-629-5074
- other than that i would maybe like a logo of a tooth, but i want it to be subtle and very basic!
- I would like the card to be preferably black or dark grey-ish with the writing in white
On the other side -
- 2-3 lines with the possibility to write the next appointment the box with the lines should be white, with the rest of the card being black

```html
<!DOCTYPE html>
<html lang="en">
<head>
<meta charset="utf-8">
<title>Dr Marlo Vintner – Business Card</title>
<link rel="stylesheet" href="https://fonts.googleapis.com/css2?family=Questrial&display=swap">
<style>
  :root {
    --backdrop: #1f1f20;
    --card-black: #1b1b1c;
    --card-edge: #262627;
    --paper: #ffffff;
    --ink: #1a1a1a;
    --text-light: #ffffff;
    --accent: #00aeef;
    --faint: rgba(255,255,255,0.05);
  }
  html, body {
    margin: 0;
    width: 1200px;
    height: 1200px;
    overflow: hidden;
    background: var(--backdrop);
    font-family: "Questrial", "Century Gothic", sans-serif;
  }
  .canvas {
    position: relative;
    width: 1200px;
    height: 1200px;
  }
  .card {
    position: absolute;
    left: 130px;
    width: 940px;
    height: 537px;
    background: var(--card-black);
    box-shadow: 0 10px 30px rgba(0,0,0,0.55);
    overflow: hidden;
  }
  .card--back { top: 45px; }
  .card--front { top: 618px; }

  /* back side */
  .appointment-box {
    position: absolute;
    left: 52px;
    top: 28px;
    right: 44px;
    bottom: 44px;
    background: var(--paper);
  }
  .appointment-title {
    margin: 70px 0 0;
    text-align: center;
    font-size: 22px;
    color: var(--ink);
    letter-spacing: 0.5px;
    font-weight: 400;
  }
  .appointment-line {
    position: absolute;
    left: 130px;
    right: 60px;
    height: 1px;
    background: var(--ink);
  }
  .appointment-line:nth-of-type(1) { top: 140px; }
  .appointment-line:nth-of-type(2) { top: 210px; }
  .appointment-line:nth-of-type(3) { top: 280px; }

  /* front side */
  .brand-mark {
    position: absolute;
    left: 150px;
    top: 88px;
    display: flex;
    align-items: center;
    gap: 10px;
    color: var(--accent);
    font-size: 22px;
    letter-spacing: 1px;
  }
  .brand-mark .dot {
    width: 14px;
    height: 14px;
    border-radius: 50%;
    background: var(--accent);
  }
  .faint-circle {
    position: absolute;
    right: -60px;
    top: 120px;
    width: 360px;
    height: 360px;
    border-radius: 50%;
    background: var(--faint);
  }
  .identity {
    position: absolute;
    left: 260px;
    top: 140px;
  }
  .doctor-name {
    margin: 0;
    font-size: 46px;
    font-weight: 400;
    color: var(--text-light);
    text-transform: uppercase;
    letter-spacing: 1px;
    line-height: 1;
  }
  .doctor-title {
    margin: 6px 0 0;
    font-size: 26px;
    color: var(--accent);
    letter-spacing: 0.5px;
  }
  .divider {
    position: absolute;
    left: 150px;
    right: 95px;
    top: 305px;
    height: 1px;
    background: var(--text-light);
  }
  .phone {
    position: absolute;
    left: 120px;
    top: 258px;
    display: flex;
    align-items: center;
    gap: 12px;
    font-size: 30px;
    color: var(--text-light);
    letter-spacing: 1px;
  }
  .phone-icon { width: 26px; height: 26px; }
  .address {
    position: absolute;
    right: 95px;
    top: 322px;
    margin: 0;
    text-align: right;
    font-style: normal;
    font-size: 24px;
    line-height: 1.35;
    color: var(--text-light);
    letter-spacing: 0.5px;
  }
  .swoosh {
    position: absolute;
    left: 0;
    bottom: 0;
    width: 940px;
    height: 200px;
  }
</style>
</head>
<body>
<main class="canvas">

  <section class="card card--back" aria-label="Appointment side">
    <div class="appointment-box">
      <h2 class="appointment-title">Appointment</h2>
      <div class="appointment-line"></div>
      <div class="appointment-line"></div>
      <div class="appointment-line"></div>
    </div>
  </section>

  <section class="card card--front" aria-label="Contact side">
    <div class="faint-circle"></div>

    <div class="brand-mark">
      <span class="dot"></span>
      <span>Vintner Dental</span>
    </div>

    <div class="identity">
      <h1 class="doctor-name">Dr Marlo Vintner</h1>
      <p class="doctor-title">Doctor of Dental Medicine</p>
    </div>

    <div class="phone">
      <svg class="phone-icon" viewBox="0 0 26 26" aria-hidden="true">
        <circle cx="13" cy="13" r="13" fill="var(--accent)"/>
        <path d="M9 7.5c.6-.4 1.3-.3 1.6.3l1 2c.3.5.1 1.1-.3 1.4l-.7.5c.5 1.3 1.4 2.4 2.6 3.1l.6-.6c.4-.4 1-.5 1.4-.2l1.9 1.2c.6.4.6 1.1.2 1.6l-.8.9c-.6.6-1.5.8-2.3.5-3.2-1.3-5.5-3.8-6.6-7-.2-.8 0-1.7.6-2.2z" fill="#fff"/>
      </svg>
      <span>514-629-5074</span>
    </div>

    <div class="divider"></div>

    <address class="address">
      5182 Ch. Birchfield<br>
      Montreal QC H2T 4B9
    </address>

    <svg class="swoosh" viewBox="0 0 940 200" preserveAspectRatio="none" aria-hidden="true">
      <path d="M0 70 C 250 150, 600 185, 940 150 L 940 200 L 0 200 Z" fill="var(--paper)"/>
      <path d="M0 105 C 260 175, 620 195, 940 160 L 940 200 L 0 200 Z" fill="var(--card-black)"/>
      <path d="M0 125 C 280 190, 640 205, 940 140 L 940 200 L 0 200 Z" fill="var(--accent)"/>
    </svg>
  </section>

</main>
</body>
</html>
```